New Meal Prep Flyer for New Package Deals

We are looking for a design that displays our new packages that we offer. If you take a look at our website www.brambleforkmeals.com, and click on packages , you'll see the way we display them currently . We would like something similar to that in style . The first package is called "Horizon" and this package will be a 1 week package (7 days ), 2 meals a day, for a price of $195.00. The second package is called "Amber" and this package will be a 3 week package (21 days) 2 meals per day, for a price of $546.00 , the third package is a 6 week+ package (45 days), and it is called "Evergreen" , 2 meals per day , and the price is $1080.00 .
For the Amber Package , can you put next to it "Save $42.00!"
For the Evergreen Package, can you put next to it "Save $180!"
We also want our logo on the flyer (see attached), and we are just looking for a 1 page flyer , 8 1/2 x 11.

```html
<!DOCTYPE html>
<html lang="en">
<head>
<meta charset="utf-8">
<title>Bramble Fork – Packages Flyer</title>
<link rel="stylesheet" href="https://fonts.googleapis.com/css2?family=Montserrat:wght@500;700;800&family=Roboto+Condensed:wght@500;700&display=swap">
<style>
  :root{
    --green:#8dc21f;
    --green-deep:#1f6a0c;
    --green-footer:#4e9914;
    --tint:#f3f8ea;
    --grey-text:#7a7a7a;
    --ink:#333333;
    --purple:#8b78e4;
    --purple-deep:#6f5bd0;
    --card-grey:#e7e7e7;
    --orange:#d4701b;
    --yellow:#f2c42f;
    --white:#ffffff;
  }
  *{margin:0;padding:0;box-sizing:border-box}
  html,body{width:900px;height:1200px;overflow:hidden;background:var(--white)}
  .flyer{position:relative;width:900px;height:1200px;overflow:hidden;background:var(--white);font-family:"Montserrat",sans-serif}

  .backdrop-pattern{position:absolute;left:0;top:450px;width:900px;height:700px;background:var(--tint)}
  .hero{position:absolute;left:0;top:0;width:900px;height:620px}

  .brand{position:absolute;left:28px;top:44px;display:flex;align-items:center;gap:10px}
  .brand-dot{width:22px;height:22px;border-radius:50%;background:var(--green)}
  .brand-name{font-family:"Montserrat",sans-serif;font-weight:800;font-size:37px;letter-spacing:1px;color:var(--grey-text);line-height:1}
  .brand-tagline{position:absolute;left:38px;top:96px;font-family:"Montserrat",sans-serif;font-weight:800;font-size:17px;color:var(--green);letter-spacing:.2px;white-space:nowrap}
  .brand-tagline .divider{display:inline-block;margin:0 8px;font-weight:500}

  .hanger{position:absolute;top:552px;width:2px;height:56px;background:var(--green)}
  .section-title{position:absolute;left:250px;top:606px;width:408px;height:75px;background:var(--green);border-radius:6px;color:var(--white);font-family:"Montserrat",sans-serif;font-weight:800;font-size:54px;text-align:center;line-height:75px;letter-spacing:1px}

  .package{position:absolute;top:719px;width:262px;height:345px;border-radius:0 0 0 34px}
  .package--horizon{left:23px;background:var(--green)}
  .package--amber{left:315px;background:var(--card-grey)}
  .package--evergreen{left:608px;background:var(--yellow);border-radius:28px 0 0 34px}

  .package-ribbon{position:absolute;left:-6px;top:34px;width:200px;height:44px;border-radius:10px 0 0 0;color:var(--white);font-family:"Roboto Condensed",sans-serif;font-weight:700;font-size:29px;line-height:46px;padding-left:28px}
  .package--horizon .package-ribbon{background:var(--green-deep)}
  .package--amber .package-ribbon{background:var(--purple);font-weight:500}
  .package--evergreen .package-ribbon{background:var(--orange)}

  .package-badge{position:absolute;top:-6px;right:-16px;width:108px;height:108px;border-radius:50%;background:var(--white);box-shadow:0 3px 8px rgba(0,0,0,.18);display:flex;align-items:center;justify-content:center}
  .package-badge .badge-core{width:92px;height:92px;border-radius:50%;display:flex;align-items:center;justify-content:center}
  .package--horizon .badge-core{background:var(--green)}
  .package--amber .badge-core{background:var(--white)}
  .package--evergreen .badge-core{background:var(--yellow)}

  .package-features{position:absolute;left:14px;top:90px;list-style:none;font-family:"Roboto Condensed",sans-serif;font-weight:500;font-size:20px;line-height:27px}
  .package-features li{display:flex;gap:7px;margin-bottom:9px}
  .package-features .tick{flex:0 0 14px;height:14px;margin-top:7px;border-radius:50%;display:flex;align-items:center;justify-content:center}
  .package--horizon .package-features{color:var(--white)}
  .package--horizon .tick{background:var(--green-deep)}
  .package--amber .package-features{color:var(--ink)}
  .package--amber .tick{background:var(--purple)}
  .package--evergreen .package-features{color:var(--ink)}
  .package--evergreen .tick{background:var(--orange)}

  .package-price{position:absolute;left:0;top:202px;width:230px;height:58px;background:var(--white);border-radius:0 30px 30px 0;box-shadow:0 3px 8px rgba(0,0,0,.12);font-family:"Montserrat",sans-serif;font-weight:800;font-size:34px;line-height:58px;padding-left:32px}
  .package--horizon .package-price{color:var(--green-deep)}
  .package--amber .package-price{color:var(--purple-deep);padding-left:27px}
  .package--evergreen .package-price{color:var(--orange);padding-left:32px}

  .package-saving{position:absolute;left:0;right:0;top:284px;height:51px;display:flex;align-items:center}
  .saving-label{font-family:"Roboto Condensed",sans-serif;font-weight:500;font-size:22px;color:var(--ink);letter-spacing:.5px;padding-left:28px;width:82px}
  .package--evergreen .saving-label{padding-left:24px;width:78px}
  .saving-amount{flex:1;height:51px;color:var(--white);font-family:"Montserrat",sans-serif;font-weight:800;font-size:32px;line-height:51px;padding-left:14px;white-space:nowrap;clip-path:polygon(8% 0,100% 0,100% 100%,8% 100%,0 50%)}
  .package--amber .saving-amount{background:var(--purple)}
  .package--evergreen .saving-amount{background:var(--orange)}

  .footer{position:absolute;left:0;top:1138px;width:900px;height:62px;background:var(--green-footer)}
  .footer-rule{position:absolute;left:0;top:1112px;width:900px;height:40px}
  .store-badge{position:absolute;top:1161px;width:74px;height:25px;border-radius:3px}
  .store-badge--one{left:39px;background:#2c2c2c}
  .store-badge--two{left:123px;background:var(--white)}
  .footer-url{position:absolute;left:250px;top:1160px;width:440px;text-align:center;color:var(--white);font-family:"Montserrat",sans-serif;font-weight:500;font-size:18px;letter-spacing:2px;line-height:28px;white-space:nowrap}
  .social{position:absolute;top:1160px;width:26px;height:26px;border-radius:50%;background:var(--white)}
</style>
</head>
<body>
<div class="flyer">

  <div class="backdrop-pattern" role="img" aria-label="Faint line pattern of food and drink icons"></div>

  <svg class="hero" viewBox="0 0 900 620">
    <path d="M0 450 C300 575 640 585 900 488 V620 H0 Z" fill="var(--tint)"/>
    <path role="img" aria-label="Photo of a grain bowl with asparagus, beetroot, spinach, zucchini and sweet potato, plus a creamy shrimp and vegetable dish"
          d="M598 0 H900 V490 C700 560 460 575 228 548 C258 320 400 120 598 0 Z" fill="#8d8a78"/>
    <path d="M598 0 C400 120 258 320 228 548" fill="none" stroke="var(--green)" stroke-width="5"/>
    <path role="img" aria-label="Close-up photo of creamy shrimp with peppers and green beans"
          d="M78 178 C38 300 62 440 200 512 C218 392 184 262 78 178 Z" fill="#c99a6c" stroke="var(--green)" stroke-width="5"/>
    <path d="M0 448 C300 572 640 582 900 486" fill="none" stroke="var(--green)" stroke-width="4"/>
    <path d="M0 488 C300 600 640 605 900 514 L900 525 C640 618 300 612 0 500 Z" fill="var(--green)"/>
  </svg>

  <div class="brand">
    <span class="brand-dot"></span>
    <span class="brand-name">BRAMBLE FORK</span>
  </div>
  <div class="brand-tagline">HEALTHY KITCHEN<span class="divider">|</span>MEAL PREP</div>

  <span class="hanger" style="left:265px"></span>
  <span class="hanger" style="left:641px"></span>
  <h1 class="section-title">PACKAGES</h1>

  <section class="package package--horizon">
    <h2 class="package-ribbon">HORIZON</h2>
    <div class="package-badge"><div class="badge-core">
      <svg width="54" height="40" viewBox="0 0 54 40" fill="none" stroke="#fff" stroke-width="3">
        <circle cx="19" cy="20" r="13"/><circle cx="35" cy="20" r="13"/>
      </svg>
    </div></div>
    <ul class="package-features">
      <li><span class="tick"><svg width="8" height="8" viewBox="0 0 8 8"><path d="M1 4 L3 6 L7 1.5" stroke="#fff" stroke-width="1.6" fill="none"/></svg></span><span>1 week /<br>7 days Package</span></li>
      <li><span class="tick"><svg width="8" height="8" viewBox="0 0 8 8"><path d="M1 4 L3 6 L7 1.5" stroke="#fff" stroke-width="1.6" fill="none"/></svg></span><span>2 meals a day</span></li>
    </ul>
    <div class="package-price">$195.00</div>
  </section>

  <section class="package package--amber">
    <h2 class="package-ribbon">AMBER</h2>
    <div class="package-badge"><div class="badge-core">
      <svg width="50" height="46" viewBox="0 0 50 46" fill="none" stroke="var(--purple)" stroke-width="3" stroke-linejoin="round">
        <path d="M25 42 C10 31 4 23 4 14 C4 7 9 3 15 3 C20 3 23 6 25 10 C27 6 30 3 35 3 C41 3 46 7 46 14 C46 23 40 31 25 42 Z"/>
      </svg>
    </div></div>
    <ul class="package-features">
      <li><span class="tick"><svg width="8" height="8" viewBox="0 0 8 8"><path d="M1 4 L3 6 L7 1.5" stroke="#fff" stroke-width="1.6" fill="none"/></svg></span><span>3 week /<br>21 days Package</span></li>
      <li><span class="tick"><svg width="8" height="8" viewBox="0 0 8 8"><path d="M1 4 L3 6 L7 1.5" stroke="#fff" stroke-width="1.6" fill="none"/></svg></span><span>2 meals a day</span></li>
    </ul>
    <div class="package-price">$546.00</div>
    <div class="package-saving"><span class="saving-label">SAVE</span><span class="saving-amount">$42.00!</span></div>
  </section>

  <section class="package package--evergreen">
    <h2 class="package-ribbon">EVERGREEN</h2>
    <div class="package-badge"><div class="badge-core">
      <svg width="52" height="44" viewBox="0 0 52 44" fill="none" stroke="var(--orange)" stroke-width="3" stroke-linejoin="round">
        <path d="M6 4 H46 V28 H22 L12 38 V28 H6 Z"/>
        <circle cx="17" cy="16" r="2" fill="var(--orange)"/><circle cx="26" cy="16" r="2" fill="var(--orange)"/><circle cx="35" cy="16" r="2" fill="var(--orange)"/>
      </svg>
    </div></div>
    <ul class="package-features">
      <li><span class="tick"><svg width="8" height="8" viewBox="0 0 8 8"><path d="M1 4 L3 6 L7 1.5" stroke="#fff" stroke-width="1.6" fill="none"/></svg></span><span>6 week+ /<br>45 days Package</span></li>
      <li><span class="tick"><svg width="8" height="8" viewBox="0 0 8 8"><path d="M1 4 L3 6 L7 1.5" stroke="#fff" stroke-width="1.6" fill="none"/></svg></span><span>2 meals a day</span></li>
    </ul>
    <div class="package-price">$1080.00</div>
    <div class="package-saving"><span class="saving-label">SAVE</span><span class="saving-amount">$180.00!</span></div>
  </section>

  <svg class="footer-rule" viewBox="0 0 900 40" preserveAspectRatio="none" aria-hidden="true">
    <path d="M0 26 C300 6 600 6 900 26 V40 H0 Z" fill="var(--green)"/>
    <path d="M0 32 C300 14 600 14 900 32" fill="none" stroke="#fff" stroke-width="3"/>
  </svg>
  <footer class="footer"></footer>
  <span class="store-badge store-badge--one"></span>
  <span class="store-badge store-badge--two"></span>
  <div class="footer-url">WWW.BRAMBLEFORKMEALS.COM</div>
  <span class="social" style="left:709px"></span>
  <span class="social" style="left:741px"></span>
  <span class="social" style="left:772px"></span>

</div>
</body>
</html>
```